Buttons, Banners & MPUs - 'Alpine Getaway Journal'

We are launching a new product - a bookazine on sale later this month!

General description below:

ALPINE GETAWAY JOURNALS 2015

Calling all lovers of French holidays! Where will you go in 2015?

Let us guide you to the very best holidays in France with our brand new guide, featuring 180 pages of high quality and inspiring editorial and imagery. Alpine Getaway Journals 2015 provides a comprehensive, ideas-packed guide to classic breaks, as well as niche and new holiday ideas across France.

Love to get out in the French fresh air? We have activities such as boating, cycling and golf covered. There’s plenty for culture vultures and city breakers, too, plus lots of great ideas for family breaks including theme parks, zoos and attractions.

We whet the appetite of foodies and wine lovers, provide a guide to markets and festivals and also get off the beaten track with guides to driving, railway holidays and visit some of France’s most beautiful villages. And if you want to get creative, there are loads of ideas for photography, art, ‘me time’ escapes and tempting snapshots of some of France’s most unusual accommodation.

Whatever you love about France, there’s a fabulous French holiday made for you!

Design brief - bright, fun, exciting, inspiring.. with a clear call-to-action

We require a variety of sizes including:
300 x 250, 250 x 250, 728 x 90, 468 x 60, 120 x 600, 120 x 240, 600 x 200
- please only create a couple to showcase your design

More information can be found on the products website but please be aware that this is still under construction so please do not base your design on this: http://www.alpinegetawayjournals.com/

Target Market(s)

Francophiles, holiday makers, 40+, families, couples,

Font styles to use
Serif
Sans Serif

Requirements
Must have
• Logo
• Call to action
Nice to have
• Suggested strap lines:
• - The ultimate guide to holidays in France
• - The biggest and best guide to France
• - 180 pages of Fabulous French Holiday Ideas
• - What's New in 2015
Should not have
• Price - we want to direct traffic to our website which will reflect their local currency

```html
<!DOCTYPE html>
<html lang="en">
<head>
<meta charset="utf-8">
<title>Alpine Getaway Journal – Banner Set</title>
<link rel="stylesheet" href="https://fonts.googleapis.com/css2?family=Oswald:wght@500;600&family=Open+Sans:wght@400;600&family=Noto+Serif:wght@700&display=swap">
<style>
:root{
  --sky-top:#7cbfea;
  --sky-bottom:#e8f4fc;
  --navy:#0b1150;
  --navy-deep:#060a35;
  --yellow:#e4f400;
  --white:#ffffff;
  --green:#2f9e2f;
  --green-dark:#1f7a22;
  --blue-btn:#15287a;
  --ink:#0d1a5a;
  --label:#1b1b1b;
}
*{box-sizing:border-box;margin:0;padding:0}
html,body{width:1200px;height:857px;overflow:hidden}
body{
  position:relative;
  background:linear-gradient(180deg,var(--sky-top) 0%,#b7dcf4 45%,var(--sky-bottom) 100%);
  font-family:"Open Sans",sans-serif;
}
.size-label{
  position:absolute;transform:translateX(-50%);
  font-family:"Open Sans",sans-serif;font-size:15px;color:var(--label);white-space:nowrap;
}
.banner{position:absolute;overflow:hidden;border:1px solid #1a1a2a;color:var(--white)}
.photo{position:absolute;inset:0}
.brand{
  position:absolute;font-family:"Oswald",sans-serif;font-weight:600;color:var(--white);
  line-height:1;white-space:nowrap;letter-spacing:-.3px;
}
.url{position:absolute;font-family:"Open Sans",sans-serif;white-space:nowrap}
.cta{
  position:absolute;display:flex;align-items:center;justify-content:center;
  font-family:"Open Sans",sans-serif;font-size:12px;color:var(--white);
  border-radius:2px;white-space:nowrap;
}
.cta--green{background:linear-gradient(180deg,#3cb43c,var(--green-dark));border-bottom:2px solid #155c17}
.cta--blue{background:linear-gradient(180deg,#2540a0,var(--blue-btn));font-weight:600;font-size:11px;border-bottom:2px solid #0a1650}
.cta--lime{background:linear-gradient(180deg,#f0fa30,#d4e400);color:#111;font-weight:600;font-size:11px}
.cond{font-family:"Oswald",sans-serif;font-weight:600;line-height:1.05}
.serif{font-family:"Noto Serif",serif;font-weight:700;line-height:1}
.y{color:var(--yellow)}
.w{color:var(--white)}

/* 300 x 250 */
.mpu{left:158px;top:116px;width:258px;height:215px}
.mpu .photo{background:linear-gradient(180deg,var(--navy-deep) 0%,#0d1a6a 55%,#1d4fb0 78%,#0a1450 100%)}
.mpu .brand{left:12px;top:8px;font-size:23px}
.mpu .pitch{position:absolute;left:13px;top:50px}
.mpu .pitch .big{font-size:25px}
.mpu .pitch .mid{font-size:16px}
.mpu .pitch .hi{font-size:19px}
.mpu .cta{left:74px;top:155px;width:112px;height:29px}
.mpu .url{left:20px;bottom:6px;font-size:13px;color:var(--yellow)}

/* 250 x 250 */
.square{left:462px;top:115px;width:216px;height:215px}
.square .photo{background:linear-gradient(180deg,#1f63c8 0%,#6fa8e0 30%,#9a9c8a 48%,#5e7a4a 65%,#3aa0b8 82%,#2b8aa6 100%)}
.square .shade{position:absolute;right:0;top:52px;width:86px;height:112px;background:rgba(6,10,53,.72)}
.square .brand{left:5px;top:8px;font-size:20px}
.square .pitch{position:absolute;right:6px;top:52px;text-align:right}
.square .pitch .s{font-size:13px}
.square .pitch .l{font-size:18px}
.square .cta{left:63px;top:164px;width:112px;height:28px}
.square .url{left:5px;bottom:4px;font-size:12px;color:var(--white)}

/* 728 x 90 */
.leader{left:157px;top:381px;width:626px;height:79px}
.leader .photo{background:linear-gradient(90deg,#5c8a98 0%,#4e8c8e 40%,#3f7f96 65%,#7b8a4a 85%,#8a8d50 100%)}
.leader .panel{position:absolute;left:0;top:0;bottom:0;width:253px;background:linear-gradient(90deg,var(--navy-deep),#0f1d60)}
.leader .brand{left:12px;top:8px;font-size:26px}
.leader .url{left:18px;bottom:5px;font-size:13px;color:var(--white)}
.leader .pitch{position:absolute;left:292px;top:6px;text-align:center}
.leader .pitch .s{font-size:14px}
.leader .pitch .l{font-size:23px}
.leader .cta{left:491px;top:24px;width:112px;height:29px}

/* 468 x 60 */
.full{left:155px;top:516px;width:396px;height:53px;border-color:#5a6a8a}
.full .photo{background:linear-gradient(180deg,#bfe3f6 0%,#8ccbee 60%,#a9d9f2 100%)}
.full .brand{left:7px;top:4px;font-size:19px;color:var(--ink)}
.full .url{left:7px;bottom:3px;font-size:10px;color:var(--ink)}
.full .pitch{position:absolute;left:183px;top:6px;text-align:center;color:var(--ink);font-size:16px}
.full .cta{left:276px;top:11px;width:118px;height:30px}

/* 600 x 200 */
.wide{left:161px;top:616px;width:516px;height:173px}
.wide .photo{background:linear-gradient(100deg,#0c1660 0%,#1a3a8a 30%,#5a6aa0 45%,#2a3a80 60%,#3a3050 80%,#8a6030 100%)}
.wide .pitch{position:absolute;left:12px;top:20px;width:150px;text-align:center}
.wide .pitch .s{font-size:21px}
.wide .pitch .l{font-size:35px}
.wide .brand{right:12px;top:14px;font-size:26px}
.wide .url{left:312px;top:70px;font-size:10px;color:var(--white)}
.wide .cta{left:389px;top:126px;width:112px;height:29px;font-family:"Noto Serif",serif;font-weight:400;font-size:11px}

/* 120 x 600 */
.sky{left:914px;top:129px;width:104px;height:516px}
.sky .photo{background:linear-gradient(180deg,#1b2266 0%,#3a3490 20%,#6a5aa8 38%,#2a2478 48%,#1a1a60 70%,#221d6a 100%)}
.sky .brand{left:0;right:0;top:6px;font-size:13px;text-align:center;white-space:normal}
.sky .pitch{position:absolute;left:0;right:0;top:228px;text-align:center}
.sky .pitch .xl{font-size:36px}
.sky .pitch .l{font-size:30px}
.sky .pitch .m{font-size:20px}
.sky .pitch .h{font-size:27px}
.sky .cta{left:6px;top:473px;width:94px;height:24px;font-family:"Noto Serif",serif;font-size:12px}
</style>
</head>
<body>

<span class="size-label" style="left:296px;top:88px">300 x 250</span>
<section class="banner mpu">
  <div class="photo" role="img" aria-label="Night city skyline with an illuminated tower"></div>
  <div class="brand">Alpine Getaway Journal</div>
  <div class="pitch cond">
    <div class="big y">180 pages</div>
    <div class="mid w">of Fabulous</div>
    <div class="mid w">French</div>
    <div class="hi y">Holiday Ideas</div>
  </div>
  <a class="cta cta--green">CALL FOR ACTION</a>
  <div class="url">www.alpinegetawayjournals.com</div>
</section>

<span class="size-label" style="left:566px;top:88px">250 x 250</span>
<section class="banner square">
  <div class="photo" role="img" aria-label="Gothic cathedral beside a river under blue sky"></div>
  <div class="shade"></div>
  <div class="brand">Alpine Getaway Journal</div>
  <div class="pitch cond">
    <div class="s w">The</div>
    <div class="l y">Ultimate</div>
    <div class="s w">Guide</div>
    <div class="s w">to Holidays</div>
    <div class="l y">France</div>
  </div>
  <a class="cta cta--lime">CALL FOR ACTION</a>
  <div class="url">www.alpinegetawayjournals.com</div>
</section>

<span class="size-label" style="left:295px;top:357px">728 x 90</span>
<section class="banner leader">
  <div class="photo" role="img" aria-label="River winding through a green valley"></div>
  <div class="panel"></div>
  <div class="brand">Alpine Getaway Journal</div>
  <div class="url">www.alpinegetawayjournals.com</div>
  <div class="pitch serif">
    <div class="s w">The</div>
    <div><span class="l y">Biggest</span> <span class="s w">&amp; best</span></div>
    <div><span class="l y">Guide</span> <span class="s w">to France</span></div>
  </div>
  <a class="cta cta--blue">CALL FOR ACTION</a>
</section>

<span class="size-label" style="left:292px;top:496px">468 x 60</span>
<section class="banner full">
  <div class="photo" role="img" aria-label="Pale blue summer sky"></div>
  <div class="brand">Alpine Getaway Journal</div>
  <div class="url">www.alpinegetawayjournals.com</div>
  <div class="pitch cond"><div>What's New</div><div>in 2015</div></div>
  <a class="cta cta--green">CALL FOR ACTION</a>
</section>

<span class="size-label" style="left:296px;top:594px">600x200</span>
<section class="banner wide">
  <div class="photo" role="img" aria-label="Glass pyramid before a lit palace at dusk"></div>
  <div class="pitch serif">
    <div class="s w">The</div>
    <div class="l y">Biggest</div>
    <div class="s w">and best</div>
    <div><span class="l y">Guide</span> <span class="s w">to</span></div>
    <div class="s w">France</div>
  </div>
  <div class="brand">Alpine Getaway Journal</div>
  <div class="url">www.alpinegetawayjournals.com</div>
  <a class="cta cta--green">CALL FOR ACTION</a>
</section>

<span class="size-label" style="left:962px;top:102px">120x600</span>
<section class="banner sky">
  <div class="photo" role="img" aria-label="Illuminated iron tower against a violet evening sky"></div>
  <div class="brand">Alpine Getaway Journal</div>
  <div class="pitch cond">
    <div class="xl y">180</div>
    <div class="l y">pages</div>
    <div class="m w">of</div>
    <div class="m w">Fabulous</div>
    <div class="m w">French</div>
    <div class="h y">Holiday</div>
    <div class="h y">Ideas</div>
  </div>
  <a class="cta cta--green">Call for Action</a>
</section>

</body>
</html>
```